K&R Security Services PTY. LTD.

Ive just had my logo made and I'm looking for some simple but strong designs for my business cards the company is a security company.

Please use dark colors.

Regards,

Owen Deloit

Reason: Need more time for discussion with other directors

Industry/Entity Type

Security

Font styles to use
Sans Serif
Decorative

```html
<!DOCTYPE html>
<html lang="en">
<head>
<meta charset="utf-8">
<title>K&amp;R Security Services – Business Cards</title>
<link rel="stylesheet" href="https://fonts.googleapis.com/css2?family=Lato:wght@300;400;700&family=Montserrat:wght@600&display=swap">
<style>
  :root {
    --bg: #d9d9d9;
    --card: #050505;
    --band: #2b2b2b;
    --band-light: #3a3a3a;
    --rule: #4a4a4a;
    --text-soft: #9a9a9a;
    --text-mid: #bdbdbd;
    --text-bright: #ffffff;
    --mark-square: #8a8a8a;
  }
  * { box-sizing: border-box; margin: 0; padding: 0; }
  html, body {
    width: 1200px; height: 926px; overflow: hidden;
    background: var(--bg);
    font-family: "Lato", sans-serif;
  }
  .canvas { position: relative; width: 1200px; height: 926px; }

  .card {
    position: absolute; left: 250px; width: 700px; height: 400px;
    background: var(--card); overflow: hidden;
    box-shadow: 0 6px 18px rgba(0,0,0,.25);
  }
  .card--front { top: 50px; }
  .card--back { top: 476px; }

  .brand {
    display: flex; align-items: center; gap: 10px;
    font-family: "Lato", sans-serif; font-weight: 700;
    color: var(--text-mid); letter-spacing: 1px;
  }
  .brand__square { width: 14px; height: 14px; background: var(--mark-square); }

  /* front */
  .card--front .brand {
    position: absolute; top: 110px; left: 0; right: 0;
    justify-content: center; font-size: 44px;
  }
  .card--front .brand__square { width: 20px; height: 20px; }
  .front__company {
    position: absolute; top: 250px; left: 0; right: 0; text-align: center;
    color: var(--text-soft); font-size: 20px; letter-spacing: 3px;
    text-transform: uppercase; font-weight: 400;
  }

  /* back */
  .back__band {
    position: absolute; left: 0; right: 0; bottom: 0; height: 46px;
    background: var(--band); border-top: 6px solid var(--band-light);
  }
  .back__divider {
    position: absolute; left: 300px; top: 40px; bottom: 80px;
    width: 1px; background: var(--rule);
  }
  .back__person {
    position: absolute; left: 0; top: 0; width: 300px; padding: 50px 24px 0;
    text-align: right;
  }
  .back__person .brand { justify-content: center; font-size: 32px; margin-bottom: 70px; }
  .person__name {
    font-family: "Montserrat", sans-serif; font-weight: 600;
    color: var(--text-bright); font-size: 22px; letter-spacing: 1.5px;
    text-align: center; margin-bottom: 16px;
  }
  .person__line { color: var(--text-bright); font-size: 13px; line-height: 20px; }
  .person__line span { color: var(--text-soft); }

  .back__company {
    position: absolute; left: 330px; top: 40px;
    color: var(--text-soft); font-size: 21px; font-weight: 400;
  }
  .back__contact {
    position: absolute; left: 330px; bottom: 80px;
    color: var(--text-soft); font-size: 15px; line-height: 22px; letter-spacing: .5px;
  }
  .back__contact .phones { font-size: 18px; }
</style>
</head>
<body>
<main class="canvas">
  <section class="card card--front">
    <div class="brand"><span class="brand__square"></span>K&amp;R Halvern</div>
    <p class="front__company">K&amp;R Security Services PTY. LTD.</p>
  </section>

  <section class="card card--back">
    <div class="back__person">
      <div class="brand"><span class="brand__square"></span>K&amp;R Halvern</div>
      <p class="person__name">OWEN</p>
      <p class="person__line"><span>email:</span> owen@halvern.net.au</p>
      <p class="person__line"><span>business email:</span> K.R@halvern.net.au</p>
    </div>
    <div class="back__divider"></div>
    <p class="back__company">K&amp;R Security Services PTY. LTD.</p>
    <div class="back__contact">
      <p>P.O. Box 7 Ashgrove Victoria 3188</p>
      <p class="phones">m: 0491570156 &nbsp;|&nbsp; p: (03) 55501234</p>
    </div>
    <div class="back__band"></div>
  </section>
</main>
</body>
</html>
```